CD face & Jewel Case Design for Bayou Lanternmen Band

We need CD packaging (jewel case with 2 panel insert, and CD disc face) designed for the band Bayou Lanternmen.

Hear a sample of the music at: https://clipvault.example/watch/kq7Lm2Xz

It should say "Bayou Lanternmen" prominently on the cover and disc face since that's the album name too. The final design should communicate fun, energy and appeal to all ages.

There are many photos to choose from and we encourage you to be creative and follow your muse.

The text for album credits/liner notes is in the file "TEXT CREDITS".

We are open to your ideas. The templates have been uploaded as .psd files - if you need in another format, please specify thanks :)

Target Market(s)

fans of zydeco music, rock, counrty, all ages

Requirements
Nice to have
• maybe a retro look but not mandatory

```html
<!DOCTYPE html>
<html lang="en">
<head>
<meta charset="utf-8">
<title>Bayou Lanternmen – CD Tray Back &amp; Disc Face</title>
<link rel="stylesheet" href="https://fonts.googleapis.com/css2?family=Montserrat:wght@700;800;900&family=Roboto+Condensed:wght@300;400&display=swap">
<style>
  :root {
    --sheet: #ffffff;
    --ink: #0b0b0b;
    --panel: #0d0d0d;
    --band-grey: #7a7a7a;
    --label-grey: #8a8a8a;
    --title-grey: #6f6f6f;
    --paper: #ffffff;
    --dash-green: #8fd18f;
    --hole-blue: #5b9bd5;
    --crop: #222222;
  }
  html, body { margin: 0; padding: 0; overflow: hidden; background: var(--sheet); }
  .sheet { width: 1200px; height: 1200px; display: block; overflow: hidden; }
  .crop-mark { stroke: var(--crop); stroke-width: 1; }
  .side-title { font-family: "Montserrat", sans-serif; font-weight: 800; font-size: 18px; letter-spacing: 1px; }
  .side-title .dim { fill: var(--title-grey); }
  .side-title .bright { fill: var(--paper); }
  .band-outline { font-family: "Montserrat", sans-serif; font-weight: 900; font-size: 132px; fill: none; stroke: var(--paper); stroke-width: 2; }
  .band-solid { font-family: "Montserrat", sans-serif; font-weight: 900; font-size: 102px; fill: var(--paper); }
  .side-label { font-family: "Roboto Condensed", sans-serif; font-weight: 400; font-size: 10px; fill: var(--label-grey); }
  .track { font-family: "Roboto Condensed", sans-serif; font-weight: 300; font-size: 15.5px; fill: var(--paper); }
  .footer-links { font-family: "Roboto Condensed", sans-serif; font-weight: 400; font-size: 9px; fill: var(--paper); }
  .view-label { font-family: "Roboto Condensed", sans-serif; font-weight: 400; fill: var(--ink); }
  .wordmark { font-family: "Montserrat", sans-serif; font-weight: 800; fill: var(--paper); }
  .disc-title-dim { font-family: "Montserrat", sans-serif; font-weight: 900; font-size: 38px; fill: var(--title-grey); }
  .disc-title-bright { font-family: "Montserrat", sans-serif; font-weight: 900; font-size: 38px; fill: var(--paper); }
  .disc-label { font-family: "Roboto Condensed", sans-serif; font-size: 9px; fill: var(--label-grey); }
  .disc-track { font-family: "Roboto Condensed", sans-serif; font-weight: 300; font-size: 10.5px; fill: var(--paper); }
</style>
</head>
<body>
<svg class="sheet" viewBox="0 0 1200 1200" xmlns="http://www.w3.org/2000/svg">
  <defs>
    <linearGradient id="photo-warm" x1="0" y1="0" x2="0" y2="1">
      <stop offset="0" stop-color="#2a1a10"/><stop offset="0.5" stop-color="#7a4a2a"/><stop offset="1" stop-color="#3a2414"/>
    </linearGradient>
    <linearGradient id="photo-stage" x1="0" y1="0" x2="0" y2="1">
      <stop offset="0" stop-color="#3b1d0e"/><stop offset="0.5" stop-color="#b86a3a"/><stop offset="1" stop-color="#5a2e18"/>
    </linearGradient>
    <linearGradient id="photo-day" x1="0" y1="0" x2="0" y2="1">
      <stop offset="0" stop-color="#cfd4d8"/><stop offset="0.5" stop-color="#8a8f96"/><stop offset="1" stop-color="#3c3f44"/>
    </linearGradient>
    <linearGradient id="photo-night" x1="0" y1="0" x2="0" y2="1">
      <stop offset="0" stop-color="#0e0e12"/><stop offset="0.6" stop-color="#4a2a3a"/><stop offset="1" stop-color="#6a3a5a"/>
    </linearGradient>
    <linearGradient id="photo-drums" x1="0" y1="0" x2="0" y2="1">
      <stop offset="0" stop-color="#b8a890"/><stop offset="0.5" stop-color="#2f4f9a"/><stop offset="1" stop-color="#2f8a3a"/>
    </linearGradient>
    <linearGradient id="photo-sepia" x1="0" y1="0" x2="1" y2="1">
      <stop offset="0" stop-color="#1c1a14"/><stop offset="0.5" stop-color="#5e5a3c"/><stop offset="1" stop-color="#9c9670"/>
    </linearGradient>
  </defs>

  <g class="crop-marks">
    <line class="crop-mark" x1="67" y1="28" x2="67" y2="55"/>
    <line class="crop-mark" x1="97" y1="28" x2="97" y2="55"/>
    <line class="crop-mark" x1="745" y1="28" x2="745" y2="55"/>
    <line class="crop-mark" x1="775" y1="28" x2="775" y2="55"/>
    <line class="crop-mark" x1="26" y1="71" x2="51" y2="71"/>
    <line class="crop-mark" x1="792" y1="71" x2="820" y2="71"/>
    <line class="crop-mark" x1="26" y1="626" x2="51" y2="626"/>
    <line class="crop-mark" x1="67" y1="642" x2="67" y2="670"/>
    <line class="crop-mark" x1="97" y1="642" x2="97" y2="670"/>
  </g>

  <g class="tray-back">
    <rect x="51" y="55" width="740" height="585" fill="var(--panel)"/>
    <g class="photo-strip">
      <rect role="img" aria-label="Accordion player in straw hat on stage" x="102" y="56" width="128" height="362" fill="url(#photo-warm)"/>
      <rect role="img" aria-label="Bass guitarist on stage" x="230" y="56" width="129" height="362" fill="url(#photo-stage)"/>
      <rect role="img" aria-label="Washboard player in knit cap outdoors" x="359" y="56" width="123" height="362" fill="url(#photo-day)"/>
      <rect role="img" aria-label="Guitarist with pink guitar at night" x="482" y="56" width="136" height="362" fill="url(#photo-night)"/>
      <rect role="img" aria-label="Drummer in sunglasses at green drum kit" x="618" y="56" width="124" height="362" fill="url(#photo-drums)"/>
    </g>
    <text class="band-outline" x="118" y="342" textLength="610" lengthAdjust="spacingAndGlyphs">BAYOU</text>
    <text class="band-solid" x="108" y="418" textLength="632" lengthAdjust="spacingAndGlyphs">LANTERNMEN</text>

    <text class="side-title" transform="translate(74,236) rotate(90)"><tspan class="dim">BAYOU </tspan><tspan class="bright">LANTERNMEN</tspan></text>
    <text class="side-title" transform="translate(768,418) rotate(-90)"><tspan class="dim">BAYOU </tspan><tspan class="bright">LANTERNMEN</tspan></text>

    <g class="tracklist side-one">
      <text class="side-label" x="138" y="432">SIDE ONE</text>
      <text class="track" x="138" y="451">1<tspan x="160">Lantern On The Levee</tspan></text>
      <text class="track" x="138" y="471">2<tspan x="160">Let's Go Paddle Down</tspan></text>
      <text class="track" x="138" y="491">3<tspan x="160">Bayou Outta Balance</tspan></text>
      <text class="track" x="138" y="511">4<tspan x="160">Can't Stop My Two-Step</tspan></text>
      <text class="track" x="138" y="531">5<tspan x="160">Moonlight Over Marsh Bay</tspan></text>
      <text class="track" x="138" y="551">6<tspan x="160">Squeezebox Round Town</tspan></text>
      <text class="track" x="138" y="571">7<tspan x="160">Firefly Waltz</tspan></text>
    </g>
    <g class="tracklist side-two">
      <text class="side-label" x="347" y="432">SIDE TWO</text>
      <text class="track" x="347" y="451">8<tspan x="369">Rust And Rain</tspan></text>
      <text class="track" x="347" y="471">9<tspan x="369">Sweet Gumbo Nights</tspan></text>
      <text class="track" x="347" y="491">10<tspan x="369">Miss Cypress Creek</tspan></text>
      <text class="track" x="347" y="511">11<tspan x="368">Forty Thousand Miles Till Sunrise</tspan></text>
      <text class="track" x="347" y="531">12<tspan x="369">Cane Fields By The River</tspan></text>
    </g>

    <g class="band-wordmark">
      <rect x="593" y="452" width="151" height="101" fill="#000"/>
      <circle cx="615" cy="502" r="7" fill="var(--paper)"/>
      <text class="wordmark" x="628" y="498" font-size="15">Bayou</text>
      <text class="wordmark" x="628" y="515" font-size="15">Lanternmen</text>
    </g>

    <rect class="footer-band" x="51" y="584" width="740" height="56" fill="var(--band-grey)"/>
    <text class="footer-links" x="421" y="599" text-anchor="middle">BayouLanternmen.example  |  Friendwall: BayouLanternmen  |  Chirper: @BayouLantern  |  Snapgrid: BayouLanternmen  |  Email: lanternbooking@mailpost.example</text>
  </g>

  <text class="view-label" x="185" y="686"><tspan font-size="19">FULL VIEW </tspan><tspan font-size="31">Outside Tray (Back)</tspan></text>

  <g class="disc-face" transform="translate(824,872) rotate(-30)">
    <rect x="-280" y="-280" width="560" height="560" fill="var(--panel)"/>
    <path role="img" aria-label="Sepia-toned group photo of the five band members with instruments" d="M-110 280 L-60 120 L60 40 L160 -40 L280 -60 L280 280 Z" fill="url(#photo-sepia)"/>
    <circle cx="0" cy="0" r="264" fill="none" stroke="var(--dash-green)" stroke-width="1.5" stroke-dasharray="6 4"/>
    <circle cx="0" cy="0" r="72" fill="none" stroke="var(--dash-green)" stroke-width="1.5" stroke-dasharray="6 4"/>
    <circle cx="0" cy="0" r="36" fill="none" stroke="var(--hole-blue)" stroke-width="1"/>

    <g class="disc-wordmark">
      <circle cx="-72" cy="-208" r="6" fill="var(--paper)"/>
      <text class="wordmark" x="-60" y="-204" font-size="14">Bayou Lanternmen</text>
    </g>
    <text x="-205" y="-112" textLength="400" lengthAdjust="spacingAndGlyphs"><tspan class="disc-title-dim">BAYOU</tspan><tspan class="disc-title-bright">LANTERNMEN</tspan></text>

    <g class="disc-tracks side-two">
      <text class="disc-label" x="105" y="-92">SIDE TWO</text>
      <text class="disc-track" x="105" y="-78">8<tspan x="119">Rust And Rain</tspan></text>
      <text class="disc-track" x="105" y="-65">9<tspan x="119">Sweet Gumbo Nights</tspan></text>
      <text class="disc-track" x="105" y="-52">10<tspan x="119">Miss Cypress Creek</tspan></text>
      <text class="disc-track" x="105" y="-39">11<tspan x="119">Forty Thousand Miles Till Sunrise</tspan></text>
      <text class="disc-track" x="105" y="-26">12<tspan x="119">Cane Fields By The River</tspan></text>
    </g>
    <g class="disc-tracks side-one">
      <text class="disc-label" x="-236" y="-38">SIDE ONE</text>
      <text class="disc-track" x="-236" y="-24">1<tspan x="-224">Lantern On The Levee</tspan></text>
      <text class="disc-track" x="-236" y="-11">2<tspan x="-224">Let's Go Paddle Down</tspan></text>
      <text class="disc-track" x="-236" y="2">3<tspan x="-224">Bayou Outta Balance</tspan></text>
      <text class="disc-track" x="-236" y="15">4<tspan x="-224">Can't Stop My Two-Step</tspan></text>
      <text class="disc-track" x="-236" y="28">5<tspan x="-224">Moonlight Over Marsh Bay</tspan></text>
      <text class="disc-track" x="-236" y="41">6<tspan x="-224">Squeezebox Round Town</tspan></text>
      <text class="disc-track" x="-236" y="54">7<tspan x="-224">Firefly Waltz</tspan></text>
    </g>
  </g>

  <text class="view-label" x="964" y="1152"><tspan font-size="31">CD Face </tspan><tspan font-size="19">FULL VIEW</tspan></text>
</svg>
</body>
</html>
```